Complete Banner Set For Web Display Ads - Including Zimbly

Ads are driving to a free web class on real estate investing made easy. The offer is for software and training that solves their number 1 challenge - Finding Deals.
Examples of copy suggestions and offer....
"Invest In Real Estate Like A Pro"
"Access Never Before Seen Inventory In Seconds"
"The Country's Best Source For Off-Market Deals"
Brody Halvaney "#1 Real Estate Investing Strategy"
Real Estate

```html
<!DOCTYPE html>
<html lang="en">
<head>
<meta charset="utf-8">
<title>Brody Halvaney – Display Banner Set</title>
<link rel="stylesheet" href="https://fonts.googleapis.com/css2?family=Arimo:wght@400;700&display=swap">
<style>
  :root {
    --page: #ffffff;
    --ink: #1f2a3c;
    --label: #333333;
    --green: #5bb12f;
    --green-edge: #93d35f;
    --blue: #1e9bd7;
    --navy: #1b2a3d;
    --slate: #2c3441;
    --photo-light: #c9c9c9;
    --photo-dark: #8f96a3;
    --cta-top: #f56a42;
    --cta-bottom: #cf3617;
    --cta-edge: #a82a10;
    --chip: #5d5f63;
    --frame: #9a9a9a;
  }
  * { box-sizing: border-box; margin: 0; padding: 0; }
  html, body { width: 1200px; height: 1200px; overflow: hidden; background: var(--page); }
  body { font-family: "Arimo", Arial, sans-serif; }

  .stage {
    position: relative;
    width: 940px; height: 940px;
    transform: scale(1.2766);
    transform-origin: 0 0;
  }

  .banner { position: absolute; overflow: hidden; border: 1px solid var(--frame); background: var(--page); }
  .banner svg.art { position: absolute; inset: 0; }
  .size-label { position: absolute; font-size: 15px; color: var(--label); }

  .photo {
    position: absolute;
    background: linear-gradient(160deg, var(--photo-light) 0%, #b3b6bc 55%, var(--photo-dark) 100%);
  }

  .title {
    position: absolute; color: var(--ink); font-weight: 700; text-align: center; line-height: 1.15;
  }
  .headline {
    position: absolute; color: #fff; font-weight: 700; text-align: center;
    text-shadow: 1px 1px 2px rgba(0,0,0,.55);
  }

  .footer { position: absolute; left: 0; right: 0; bottom: 0; background: var(--navy); }

  .cta {
    position: absolute; display: flex; align-items: center; justify-content: space-between;
    padding: 0 6px 0 10px;
    background: linear-gradient(var(--cta-top), var(--cta-bottom));
    border: 1px solid var(--cta-edge);
    border-radius: 5px;
    box-shadow: 0 1px 2px rgba(0,0,0,.4), inset 0 1px 0 rgba(255,255,255,.35);
  }
  .cta-label { color: #fff; font-weight: 700; font-size: 13px; text-shadow: 1px 1px 1px rgba(0,0,0,.45); white-space: nowrap; }
  .cta-arrow {
    width: 24px; height: 20px; border-radius: 3px; background: var(--chip);
    border: 1px solid #eee; display: flex; align-items: center; justify-content: center;
  }

  /* 728x90 */
  .leaderboard { left: 105px; top: 95px; width: 727px; height: 90px; }
  .leaderboard .title { left: 0; width: 150px; top: 8px; font-size: 16px; line-height: 18px; }
  .leaderboard .photo { left: 420px; top: 0; width: 140px; height: 90px; }
  .leaderboard .side-panel { position: absolute; left: 560px; top: 0; width: 167px; height: 90px; background: var(--slate); }
  .leaderboard .headline { left: 180px; width: 250px; top: 20px; font-size: 20px; line-height: 24px; }
  .leaderboard .cta { left: 568px; top: 28px; width: 152px; height: 35px; }

  /* 300x250 */
  .rectangle { left: 105px; top: 256px; width: 300px; height: 250px; }
  .rectangle .title { left: 0; right: 0; top: 4px; font-size: 18px; line-height: 19px; }
  .rectangle .photo { left: 150px; top: 50px; width: 150px; height: 150px; }
  .rectangle .headline { left: 5px; width: 166px; top: 77px; font-size: 21px; line-height: 24px; }
  .rectangle .footer { height: 50px; }
  .rectangle .cta { left: 75px; top: 207px; width: 153px; height: 35px; }

  /* 160x600 */
  .skyscraper { left: 662px; top: 257px; width: 160px; height: 600px; }
  .skyscraper .title { left: 0; right: 0; top: 8px; font-size: 18px; line-height: 22px; }
  .skyscraper .photo { left: 0; top: 325px; width: 160px; height: 215px; }
  .skyscraper .headline { left: 10px; width: 140px; top: 150px; font-size: 20px; line-height: 24px; }
  .skyscraper .footer { height: 62px; }
  .skyscraper .cta { left: 10px; top: 555px; width: 140px; height: 33px; padding-left: 8px; }
  .skyscraper .cta-label { font-size: 12px; }
</style>
</head>
<body>
<div class="stage">

  <!-- 728x90 leaderboard -->
  <section class="banner leaderboard">
    <div class="photo" role="img" aria-label="Portrait photo of Brody Halvaney in a blue blazer"></div>
    <div class="side-panel"></div>
    <svg class="art" width="727" height="90" viewBox="0 0 727 90">
      <path d="M150 0 H190 Q164 45 190 90 H150 Q128 45 150 0 Z" fill="var(--blue)"/>
      <path d="M188 0 H200 Q176 45 200 90 H188 Q164 45 188 0 Z" fill="#fff"/>
      <path d="M196 8 H430 L458 45 L430 82 H196 Q176 45 196 8 Z" fill="var(--green)" stroke="var(--green-edge)" stroke-width="2"/>
    </svg>
    <p class="title">Brody Halvaney<br>#1 Real Estate<br>investing<br>Strategy</p>
    <p class="headline">Invest in Real Estate<br>like a PRO</p>
    <a class="cta"><span class="cta-label">Download Now</span><span class="cta-arrow"><svg width="10" height="8" viewBox="0 0 10 8"><path d="M0 0 H10 L5 8 Z" fill="#fff"/></svg></span></a>
  </section>
  <p class="size-label" style="left:446px;top:192px;">728X90</p>

  <!-- 300x250 rectangle -->
  <section class="banner rectangle">
    <div class="photo" role="img" aria-label="Portrait photo of Brody Halvaney in a blue blazer"></div>
    <svg class="art" width="300" height="250" viewBox="0 0 300 250">
      <path d="M0 0 H300 V52 Q150 40 0 70 Z" fill="#fff"/>
      <path d="M0 70 Q150 40 300 52 V64 Q150 52 0 84 Z" fill="var(--blue)"/>
      <path d="M0 84 Q150 52 300 64 V66 Q150 56 0 88 Z" fill="#fff"/>
      <path d="M0 88 Q70 74 150 64 V200 H0 Z" fill="#fff"/>
      <path d="M8 72 Q85 60 160 58 V160 L84 184 L8 160 Z" fill="var(--green)" stroke="var(--green-edge)" stroke-width="2"/>
    </svg>
    <p class="title">Brody Halvaney #1 Real Estate<br>investing Strategy</p>
    <p class="headline">Invest in<br>Real Estate<br>like a<br>PRO</p>
    <div class="footer"></div>
    <a class="cta"><span class="cta-label">Download Now</span><span class="cta-arrow"><svg width="10" height="8" viewBox="0 0 10 8"><path d="M0 0 H10 L5 8 Z" fill="#fff"/></svg></span></a>
  </section>
  <p class="size-label" style="left:150px;top:542px;">300X250</p>

  <!-- 160x600 skyscraper -->
  <section class="banner skyscraper">
    <div class="photo" role="img" aria-label="Portrait photo of Brody Halvaney in a blue blazer"></div>
    <svg class="art" width="160" height="600" viewBox="0 0 160 600">
      <path d="M0 136 Q80 96 160 136 V148 Q80 108 0 148 Z" fill="var(--blue)"/>
      <path d="M16 128 Q80 112 144 128 V324 L80 345 L16 324 Z" fill="var(--green)" stroke="var(--green-edge)" stroke-width="2"/>
    </svg>
    <p class="title">Brody Halvaney<br>#1 Real Estate<br>investing<br>Strategy</p>
    <p class="headline">Invest in<br>Real<br>Estate<br>like<br>a<br>PRO</p>
    <div class="footer"></div>
    <a class="cta"><span class="cta-label">Download Now</span><span class="cta-arrow"><svg width="10" height="8" viewBox="0 0 10 8"><path d="M0 0 H10 L5 8 Z" fill="#fff"/></svg></span></a>
  </section>
  <p class="size-label" style="left:702px;top:863px;">160X600</p>

</div>
</body>
</html>
```